Copper and Slate Mist NZ new website!

We are a new online vaping retailer and are looking for an awesome sleek website. We are going to be selling a variety of vaping products and gear. Our logo has just been developed and we would like to keep the website in line with the black, tan a white theme. We would like to trying watermarking or imposing the rottie into the background of the website on the home page, with the page being black and you can see the tan and white colours only.

Coding

Coded - Design and coding required

Number of Pages Required

2 page

Font styles to use
Serif
Sans Serif
Decorative

Requirements
Must have
• A home page and a standard page for products
• Stay in line with the colours in the logo

```html
<!DOCTYPE html>
<html lang="en">
<head>
<meta charset="utf-8">
<title>Copper and Slate Mist NZ</title>
<link rel="stylesheet" href="https://fonts.googleapis.com/css2?family=Poppins:wght@300;400;500;600;700&family=Playfair+Display:ital@1&display=swap">
<style>
:root{
  --tan:#d2821c;
  --tan-dark:#b96c12;
  --ink:#1d1d1d;
  --ink-soft:#2a2a2a;
  --night:#161616;
  --paper:#ffffff;
  --mist:#f7f7f7;
  --grey:#8a8a8a;
  --grey-light:#bdbdbd;
  --cocoa:#3a2c27;
  --rose:#e8366c;
}
*{box-sizing:border-box;margin:0;padding:0}
html,body{width:1200px;height:3000px;overflow:hidden}
body{background:#e9e9e9;font-family:'Poppins',sans-serif;color:var(--ink)}
.page{position:absolute;left:241.7px;top:0;width:602px;height:2520px;transform:scale(1.1905);transform-origin:0 0;background:var(--paper);overflow:hidden}
.band{position:absolute;left:0;width:602px;overflow:hidden}
.abs{position:absolute}
.photo{position:absolute}

/* hero */
.hero{top:0;height:286px;background:linear-gradient(100deg,#6f6a66 0%,#8c8680 35%,#a39d96 65%,#c9c4bd 100%)}
.hero .shade{position:absolute;inset:0;background:rgba(20,16,14,.25)}
.nav{position:absolute;top:0;left:0;width:602px;height:37px;border-bottom:1px solid rgba(255,255,255,.25)}
.brand{position:absolute;left:14px;top:12px;display:flex;align-items:center;gap:5px;color:#fff;font-size:7px;font-weight:600}
.brand-dot{width:12px;height:12px;border-radius:50%;background:var(--tan)}
.nav-divider{position:absolute;left:70px;top:0;width:1px;height:37px;background:rgba(255,255,255,.25)}
.nav-links{position:absolute;top:13px;left:210px;display:flex;gap:16px;font-size:6px;color:#fff;font-weight:500}
.nav-search{position:absolute;right:8px;top:12px}
.hero-title{position:absolute;top:96px;width:100%;text-align:center;color:#fff;font-size:24px;font-weight:600;letter-spacing:-.3px}
.perks{position:absolute;top:144px;font-size:5.6px;color:#fff;line-height:13.5px}
.perks span{color:#fff;margin-right:3px;font-size:7px}
.price-tag{position:absolute;left:244px;top:208px;width:72px;height:16px;background:#fff;border-radius:2px;transform:skew(-8deg);display:flex;align-items:center;justify-content:center;font-size:7.5px;font-weight:600;color:var(--ink)}
.buy{position:absolute;left:316px;top:207px;width:50px;height:17px;background:var(--tan);color:#fff;font-size:5.6px;font-weight:600;display:flex;align-items:center;justify-content:center}
.arrow{position:absolute;top:138px}
.mouse{position:absolute;left:297px;top:260px;width:8px;height:15px;border:1px solid rgba(255,255,255,.8);border-radius:4px}

/* featured */
.featured{top:286px;height:145px;background:var(--paper)}
.kicker{position:absolute;left:84px;top:28px;font-family:'Playfair Display',serif;font-style:italic;font-size:5.5px;color:var(--grey)}
.featured h2{position:absolute;left:84px;top:40px;font-size:16.5px;font-weight:600;letter-spacing:-.4px}
.featured p{position:absolute;left:84px;top:76px;width:160px;font-size:7px;line-height:13px;color:var(--grey);font-weight:300}

/* features */
.features{top:431px;height:348px;background:var(--night)}
.features .strip{position:absolute;top:0;left:0;width:100%;height:39px;background:#0f0f0f}
.features h2{position:absolute;top:49px;width:100%;text-align:center;color:#fff;font-size:16.5px;font-weight:600}
.features .lead{position:absolute;top:78px;left:170px;width:262px;text-align:center;color:#ddd;font-size:7.5px;line-height:12.5px;font-weight:300}
.perk{position:absolute;width:120px}
.perk h4{font-size:5.6px;font-weight:700;color:#fff;margin-bottom:4px}
.perk p{font-size:5.2px;line-height:9.8px;color:#aaa;font-weight:300}
.perk.left{text-align:right;left:72px}
.perk.right{left:413px}
.perk-icon{position:absolute;width:22px;height:22px;border-radius:50%;background:var(--tan);display:flex;align-items:center;justify-content:center}
.to-top{position:absolute;width:13px;height:13px;background:#6f6f6f;display:flex;align-items:center;justify-content:center}

/* gallery */
.gallery-head{top:779px;height:72px;background:var(--mist)}
.gallery-head h2{position:absolute;top:16px;width:100%;text-align:center;font-size:15px;font-weight:600;color:#333}
.gallery-head p{position:absolute;top:39px;width:100%;text-align:center;font-size:5.6px;color:var(--grey)}
.gallery{top:851px;height:188px;background:#222}

/* compare */
.compare{top:1039px;height:206px;background:var(--mist)}
.compare h2{position:absolute;left:84px;top:58px;font-size:13px;font-weight:500;letter-spacing:-.3px}
.compare p{position:absolute;left:84px;top:88px;width:215px;font-size:7px;line-height:13.5px;color:var(--grey);font-weight:300}
.pill{position:absolute;height:16px;border-radius:8px;background:#3a3a3a;color:#fff;font-size:5.8px;font-weight:500;display:flex;align-items:center;justify-content:center}
.lung-card{position:absolute;left:307px;top:26px;width:213px;height:155px;background:#fff;box-shadow:0 1px 4px rgba(0,0,0,.2)}

/* videos */
.videos{top:1245px;height:209px}
.video{position:absolute;top:0;width:301px;height:209px}
.video h3{position:absolute;left:25px;top:26px;color:#fff;font-size:8.5px;font-weight:700}
.video .sub{position:absolute;left:25px;top:44px;color:#eee;font-size:6.8px;font-weight:300}
.video .body{position:absolute;left:25px;top:132px;width:240px;color:#eee;font-size:5.4px;line-height:10px;font-weight:300}
.play{position:absolute;left:25px;top:159px;display:flex;align-items:center;gap:6px;color:#fff;font-size:5.3px;font-weight:700}
.play i{width:18px;height:18px;border:1px solid #fff;border-radius:50%;display:flex;align-items:center;justify-content:center}

/* categories */
.cat-head{top:1454px;height:46px;background:var(--paper)}
.cat-head h2{position:absolute;top:18px;width:100%;text-align:center;font-size:15px;font-weight:600;color:#222}
.categories{top:1500px;height:246px;background:#c9c9c9}
.cat{position:absolute;top:0;width:200px;height:246px}
.cat h3{position:absolute;top:131px;width:100%;text-align:center;color:#fff;font-size:11px;font-weight:500}
.cat p{position:absolute;top:148px;width:100%;text-align:center;color:#fff;font-size:5px;font-weight:300}

/* membership */
.membership{top:1746px;height:380px;background:linear-gradient(180deg,#3a2d29 0%,#433330 40%,#3a2c27 100%)}
.membership h2{position:absolute;top:20px;width:100%;text-align:center;color:#fff;font-size:14.5px;font-weight:600}
.membership .lead{position:absolute;top:46px;left:165px;width:272px;text-align:center;color:#9e8b84;font-size:5.5px;line-height:9.5px}
.toggle{position:absolute;top:108px;left:256px;display:flex;align-items:center;gap:8px;font-size:5.8px;color:#fff}
.switch{width:23px;height:11px;border-radius:6px;background:#17a2b8;position:relative}
.switch::after{content:"";position:absolute;left:2px;top:2px;width:7px;height:7px;border-radius:50%;background:#fff}
.toggle .off{color:#8c7a74}
.save{position:absolute;left:357px;top:102px;font-size:3.8px;color:#cbbab3}
.plan{position:absolute;top:142px;width:134px;height:203px;background:#fff;text-align:center;overflow:hidden}
.plan .tier{position:absolute;top:18px;width:100%;font-size:5.2px;color:#555;font-weight:500}
.plan .price{position:absolute;top:34px;width:100%;font-size:21px;font-weight:500;color:#222}
.plan .price sup{font-size:7px;vertical-align:10px}
.plan .term{position:absolute;top:67px;width:100%;font-size:3.8px;color:var(--grey);letter-spacing:.5px}
.plan ul{position:absolute;top:89px;left:28px;width:78px;list-style:none;font-size:5px;font-weight:600;color:#333}
.plan li{height:13px;line-height:12px;border-bottom:1px solid #eee}
.plan li:last-child{border-bottom:0}
.plan li span{font-weight:300;color:var(--grey)}
.ribbon{position:absolute;right:-16px;top:8px;width:60px;height:10px;background:var(--rose);transform:rotate(45deg);color:#fff;font-size:3.6px;line-height:10px;font-weight:700}

/* faq */
.faq{top:2126px;height:160px;background:var(--paper)}
.faq-item{position:absolute;width:170px}
.faq-item h4{font-size:7px;font-weight:500;color:#333;margin-bottom:7px}
.faq-item p{font-size:5.2px;line-height:9.8px;color:var(--grey);font-weight:300}
.faq-tick{position:absolute;width:11px;height:11px;border:1px solid var(--tan);border-radius:50%;display:flex;align-items:center;justify-content:center}

/* contact */
.contact{top:2286px;height:185px;background:linear-gradient(90deg,#eef1f4 0%,#e4e8ec 45%,#d9d3cc 70%,#ecebe8 100%)}
.contact h3{position:absolute;top:31px;font-size:8.5px;font-weight:500;color:#222}
.field-label{position:absolute;left:84px;font-size:4.6px;color:#444}
.field{position:absolute;left:84px;width:115px;height:12px;background:#fff;border:1px solid #ddd}
.outline-btn{position:absolute;left:84px;top:2417px;width:48px;height:13px;border:1px solid #444;border-radius:7px;font-size:5px;display:flex;align-items:center;justify-content:center;color:#333}
.contact .note{position:absolute;left:84px;top:148px;font-size:3.8px;color:#555}
.address{position:absolute;left:233px;top:57px;font-size:5px;line-height:8px;color:#333}
.socials{position:absolute;left:233px;top:111px;display:flex;gap:5px}
.socials i{width:11px;height:11px;border-radius:50%;background:#2f6fd0;display:block}
.socials i:last-child{background:#111}

/* footer */
.footer{top:2471px;height:49px;background:var(--paper);text-align:center}
.footer p{position:absolute;top:17px;width:100%;font-size:5px;color:#555}
.footer .links{top:27px;color:#333}
</style>
</head>
<body>
<main class="page">

  <header class="band hero">
    <div class="photo" role="img" aria-label="Woman in a leather jacket holding a vape pen in front of a pale building" style="inset:0;background:linear-gradient(100deg,#7b746e,#8a847f 40%,#b2aca5 75%,#d4cfc8)"></div>
    <div class="shade"></div>
    <nav class="nav">
      <div class="brand"><span class="brand-dot"></span>Copper and Slate Mist NZ</div>
      <div class="nav-divider"></div>
      <div class="nav-links"><span>Home</span><span>About</span><span>Products</span><span>Services</span><span>Pricing</span><span>Contacts</span></div>
      <svg class="nav-search" width="8" height="8" viewBox="0 0 8 8"><circle cx="3.3" cy="3.3" r="2.3" fill="none" stroke="#fff" stroke-width="1"/><line x1="5" y1="5" x2="7.3" y2="7.3" stroke="#fff" stroke-width="1"/></svg>
    </nav>
    <h1 class="hero-title">Healthy way to Smoke</h1>
    <div class="perks" style="left:212px"><div><span>+</span>No Lungs problem</div><div style="padding-left:16px"><span>+</span>No Tars</div><div style="padding-left:14px"><span>+</span>No poison</div><div style="padding-left:5px"><span>+</span>Easily Available</div></div>
    <div class="perks" style="left:344px"><div style="padding-left:12px"><span>+</span>1 User</div><div><span>+</span>Rechargable</div><div style="padding-left:10px"><span>+</span>Clean</div></div>
    <div class="price-tag">$29.99/m</div>
    <div class="buy">Buy Now</div>
    <svg class="arrow" style="left:4px" width="12" height="10" viewBox="0 0 12 10"><path d="M11 5H1M5 1L1 5l4 4" fill="none" stroke="#fff" stroke-width="1"/></svg>
    <svg class="arrow" style="left:586px" width="12" height="10" viewBox="0 0 12 10"><path d="M1 5h10M7 1l4 4-4 4" fill="none" stroke="#fff" stroke-width="1"/></svg>
    <div class="mouse"></div>
  </header>

  <section class="band featured">
    <div class="kicker">New Product : #2473</div>
    <h2>Featured Product!</h2>
    <p>A short description about the new vape product (featured product).</p>
    <div class="photo" role="img" aria-label="Two vape pens, one black and one silver, standing upright" style="left:445px;top:2px;width:62px;height:140px;background:linear-gradient(90deg,#1c1c1c 0%,#3a3a3a 45%,#9a9a9a 55%,#d0d0d0 100%)"></div>
  </section>

  <section class="band features">
    <div class="strip"></div>
    <h2>A Harmless kind of Addition</h2>
    <p class="lead">Lorem ipsum dolor sit amet, consectetur adipiscing elit, sed do eiusmod tempor.</p>

    <div class="perk left" style="top:126px"><h4>NO HEART DAMAGE</h4><p>Lorem ipsum dolor sit amet, consectetur adipiscing elit. Labore vero dignissimos, ipsa reiciendis quaerat.</p></div>
    <div class="perk left" style="top:186px"><h4>NO LONG LIST OF POISONS</h4><p>Lorem ipsum dolor sit amet, consectetur adipiscing elit. Labore vero dignissimos, ipsa reiciendis quaerat.</p></div>
    <div class="perk left" style="top:246px"><h4>NO LUNGS PROBLEM</h4><p>Lorem ipsum dolor sit amet, consectetur adipiscing elit. Placeat nobis maiores recusandae repellendus, tempora laudantium.</p></div>

    <div class="perk-icon" style="left:199px;top:126px"><svg width="9" height="8" viewBox="0 0 9 8"><path d="M4.5 7.5L1 4a2 2 0 0 1 3.5-2.6A2 2 0 0 1 8 4z" fill="none" stroke="#fff" stroke-width=".9"/></svg></div>
    <div class="perk-icon" style="left:199px;top:186px"><svg width="8" height="9" viewBox="0 0 8 9"><rect x="1" y="1" width="6" height="7" fill="none" stroke="#fff" stroke-width=".9"/><path d="M2.5 3h3M2.5 4.5h3M2.5 6h3" stroke="#fff" stroke-width=".7"/></svg></div>
    <div class="perk-icon" style="left:199px;top:246px"><svg width="9" height="9" viewBox="0 0 9 9"><path d="M4.5 1L8 3 4.5 5 1 3z" fill="#fff"/><path d="M1 4.8l3.5 2 3.5-2" fill="none" stroke="#fff" stroke-width=".9"/></svg></div>

    <div class="photo" role="img" aria-label="Silver and black vape pens side by side" style="left:252px;top:133px;width:98px;height:167px;background:linear-gradient(90deg,#3a3a3a,#bdbdbd 25%,#777 48%,#1e1e1e 55%,#3c3c3c 80%,#151515)"></div>

    <div class="perk-icon" style="left:383px;top:126px"><svg width="9" height="9" viewBox="0 0 9 9"><path d="M3 2.3a3 3 0 1 0 3 0" fill="none" stroke="#fff" stroke-width=".9"/><line x1="4.5" y1="1" x2="4.5" y2="4.5" stroke="#fff" stroke-width=".9"/></svg></div>
    <div class="perk-icon" style="left:383px;top:186px"><svg width="9" height="8" viewBox="0 0 9 8"><path d="M1.5 4l2 2 4-4" fill="none" stroke="#fff" stroke-width="1"/></svg></div>
    <div class="perk-icon" style="left:383px;top:246px"><svg width="8" height="9" viewBox="0 0 8 9"><path d="M2.5 5.5a2.6 2.6 0 1 1 3 0V7h-3z" fill="none" stroke="#fff" stroke-width=".8"/></svg></div>

    <div class="perk right" style="top:126px"><h4>MORE IN CONTROL</h4><p>Lorem ipsum dolor sit amet, consectetur adipiscing elit. Labore vero dignissimos, ipsa reiciendis quaerat.</p></div>
    <div class="perk right" style="top:186px"><h4>APPROVED BY ...</h4><p>Lorem ipsum dolor sit amet, consectetur adipiscing elit. Labore vero dignissimos, ipsa reiciendis quaerat.</p></div>
    <div class="perk right" style="top:246px"><h4>A BETTER WAY TO SMOKE</h4><p>Lorem ipsum dolor sit amet, consectetur adipiscing elit. Labore vero dignissimos, ipsa reiciendis quaerat.</p></div>

    <div class="to-top" style="left:579px;top:87px;background:#2a2a2a"><svg width="5" height="3" viewBox="0 0 5 3"><path d="M.5 2.5l2-2 2 2" fill="none" stroke="#ccc" stroke-width=".7"/></svg></div>
  </section>

  <section class="band gallery-head">
    <h2>Gallery</h2>
    <p>A Photo Gallery Of Vape Products</p>
  </section>

  <section class="band gallery">
    <div class="photo" role="img" aria-label="Man walking past a brick building exhaling vapour" style="left:0;top:0;width:151px;height:100px;background:linear-gradient(135deg,#4a5a4f,#8a7a6a)"></div>
    <div class="photo" role="img" aria-label="Woman vaping outdoors among greenery" style="left:152px;top:0;width:150px;height:100px;background:linear-gradient(135deg,#4d5a2c,#8f8a55)"></div>
    <div class="photo" role="img" aria-label="Close view of a vape device in a jeans pocket" style="left:303px;top:0;width:151px;height:100px;background:linear-gradient(135deg,#b9aa98,#5e6b80)"></div>
    <div class="photo" role="img" aria-label="Woman vaping by a window indoors" style="left:455px;top:0;width:147px;height:100px;background:linear-gradient(135deg,#8a9197,#d8d3cc)"></div>
    <div class="photo" role="img" aria-label="Hand holding a vape device in low light" style="left:0;top:101px;width:151px;height:87px;background:linear-gradient(135deg,#141414,#5c5f5c)"></div>
    <div class="photo" role="img" aria-label="Woman in a coat vaping in an autumn park" style="left:152px;top:101px;width:150px;height:87px;background:linear-gradient(135deg,#7c5a32,#c0974f)"></div>
    <div class="photo" role="img" aria-label="Close view of a vape mod with a digital display" style="left:303px;top:101px;width:151px;height:87px;background:linear-gradient(90deg,#cfcfcf,#6a6a6a 40%,#b58a2a 75%,#8a6418)"></div>
    <div class="photo" role="img" aria-label="Man in a beanie exhaling a large cloud of vapour" style="left:455px;top:101px;width:147px;height:87px;background:linear-gradient(135deg,#3a2e2a,#c9c4c4 55%,#7a6a62)"></div>
    <div class="to-top" style="left:579px;top:165px"><svg width="5" height="3" viewBox="0 0 5 3"><path d="M.5 2.5l2-2 2 2" fill="none" stroke="#eee" stroke-width=".7"/></svg></div>
  </section>

  <section class="band compare">
    <h2>Comparing Lungs Health</h2>
    <p>We can put 2 images of lung one for regular smoker and one for vape to compare. possible to put over each other.</p>
    <div class="pill" style="left:84px;top:142px;width:53px">Shop Now</div>
    <div class="lung-card" role="img" aria-label="Before and after slider comparing a vaper's lungs with a regular smoker's lungs" style="background:linear-gradient(90deg,#fff 0%,#f4f4f4 70%,#e9e9e9 71%,#fff 72%)"></div>
  </section>

  <section class="band videos">
    <article class="video" style="left:0">
      <div class="photo" role="img" aria-label="Young man in sunglasses exhaling vapour outdoors" style="inset:0;background:linear-gradient(135deg,#3e4a2a,#6b6a50 50%,#2a2a26)"></div>
      <h3>VIDEO 1 TITLE</h3>
      <div class="sub">a short description about the video</div>
      <p class="body">Lorem ipsum dolor sit amet, consectetur adipiscing elit, sed do eiusmod tempor incididunt ut labore et dolore magna aliqua. Ut enim ad minim veniam.</p>
      <div class="play"><i><svg width="5" height="6" viewBox="0 0 5 6"><path d="M0 0l5 3-5 3z" fill="#fff"/></svg></i>PLAY VIDEO</div>
    </article>
    <article class="video" style="left:302px;width:300px">
      <div class="photo" role="img" aria-label="Blonde woman exhaling vapour against a brick wall" style="inset:0;background:linear-gradient(90deg,#7a3a2c,#b9aca6 35%,#c8a060 75%,#6a3428)"></div>
      <h3>VIDEO 2 TITLE</h3>
      <div class="sub">A short description about the video</div>
      <p class="body">quis nostrud exercitation ullamco laboris nisi ut aliquip ex ea commodo consequat. Duis aute irure dolor in reprehenderit in voluptate velit.</p>
      <div class="play"><i><svg width="5" height="6" viewBox="0 0 5 6"><path d="M0 0l5 3-5 3z" fill="#fff"/></svg></i>PLAY VIDEO</div>
    </article>
  </section>

  <section class="band cat-head">
    <h2>Products Categories</h2>
    <div class="to-top" style="left:579px;top:21px;background:#bdbdbd"><svg width="5" height="3" viewBox="0 0 5 3"><path d="M.5 2.5l2-2 2 2" fill="none" stroke="#fff" stroke-width=".7"/></svg></div>
  </section>

  <section class="band categories">
    <div class="cat" style="left:0">
      <div class="photo" role="img" aria-label="Black and silver vape pens" style="left:52px;top:28px;width:96px;height:218px;background:linear-gradient(90deg,#151515,#3a3a3a 45%,#8a8a8a 55%,#c6c6c6)"></div>
      <h3>Product Category 1</h3><p>Description of category 1</p>
    </div>
    <div class="cat" style="left:200px">
      <div class="photo" role="img" aria-label="Green box mod vape with a tank" style="left:70px;top:50px;width:70px;height:182px;background:linear-gradient(180deg,#2a2a2a 0%,#5a5a5a 35%,#2fae3a 50%,#111 100%)"></div>
      <h3>Product Category 2</h3><p>Description of category 2</p>
    </div>
    <div class="cat" style="left:400px;width:202px">
      <div class="photo" role="img" aria-label="Black and silver box mod vapes" style="left:28px;top:52px;width:140px;height:188px;background:linear-gradient(90deg,#1c1c1c,#3c3c3c 45%,#9a9aa0 60%,#6e6e74)"></div>
      <h3>Product Category 3</h3><p>Description of category 3</p>
    </div>
    <div class="to-top" style="left:579px;top:224px;background:#a9a9a9"><svg width="5" height="3" viewBox="0 0 5 3"><path d="M.5 2.5l2-2 2 2" fill="none" stroke="#fff" stroke-width=".7"/></svg></div>
  </section>

  <section class="band membership">
    <div class="photo" role="img" aria-label="Dark, faint photo of a rottweiler behind the pricing plans" style="left:150px;top:60px;width:300px;height:120px;background:radial-gradient(ellipse at center,rgba(30,22,20,.55),rgba(58,44,39,0))"></div>
    <h2>Our Membership Plan</h2>
    <p class="lead">If There Is A Membership Option For Products Or Support Or Services We Can Put Them Here.</p>
    <div class="save">Save 20%</div>
    <div class="toggle"><span>Monthly</span><span class="switch"></span><span class="off">Annually</span></div>

    <div class="plan" style="left:86px">
      <div class="tier">STARTER</div>
      <div class="price">FREE</div>
      <div class="term">LIMITED ACCESS</div>
      <ul><li>Free Support <span>Access</span></li><li>Feature 1</li><li>Feature 2</li><li>Feature 3</li><li>Feature 4</li></ul>
      <div class="pill" style="left:36px;top:168px;width:63px;background:#2b2b2b">Get Free Trail</div>
    </div>
    <div class="plan" style="left:235px">
      <div class="ribbon">POPULAR</div>
      <div class="tier">POPULAR</div>
      <div class="price"><sup>$</sup>12</div>
      <div class="term">MONTHLY</div>
      <ul><li>Free Support <span>Access</span></li><li>Feature 1</li><li>Feature 2</li><li>Feature 3</li><li>Feature 4</li></ul>
      <div class="pill" style="left:36px;top:168px;width:63px;background:#2b2b2b">Get Started</div>
    </div>
    <div class="plan" style="left:384px">
      <div class="tier">PROFESSIONAL</div>
      <div class="price"><sup>$</sup>19</div>
      <div class="term">MONTHLY</div>
      <ul><li>Free Support <span>Access</span></li><li>Feature 1</li><li>Feature 2</li><li>Feature 3</li><li>Feature 4</li></ul>
      <div class="pill" style="left:36px;top:168px;width:63px;background:#2b2b2b">Get Started</div>
    </div>
    <div class="to-top" style="left:579px;top:232px;background:#2c211e"><svg width="5" height="3" viewBox="0 0 5 3"><path d="M.5 2.5l2-2 2 2" fill="none" stroke="#ccc" stroke-width=".7"/></svg></div>
  </section>

  <section class="band faq">
    <div class="faq-tick" style="left:121px;top:33px"><svg width="6" height="5" viewBox="0 0 6 5"><path d="M.8 2.5l1.6 1.6L5.2.8" fill="none" stroke="#d2821c" stroke-width=".8"/></svg></div>
    <div class="faq-item" style="left:138px;top:31px"><h4>F.A.Q question number 1?</h4><p>Lorem ipsum dolor sit amet, consectetur adipiscing elit, sed do eiusmod tempor incididunt ut labore et dolore magna aliqua. Ut enim ad minim veniam</p></div>
    <div class="faq-tick" style="left:307px;top:33px"><svg width="6" height="5" viewBox="0 0 6 5"><path d="M.8 2.5l1.6 1.6L5.2.8" fill="none" stroke="#d2821c" stroke-width=".8"/></svg></div>
    <div class="faq-item" style="left:324px;top:31px"><h4>F.A.Q question number 2?</h4><p>Cras sit amet nibh libero, in gravida nulla. Nulla vel metus scelerisque ante sollicitudin. Cras purus odio, vestibulum in vulputate at, tempus viverra turpis. Fusce condimentum.</p></div>
    <div class="faq-tick" style="left:121px;top:97px"><svg width="6" height="5" viewBox="0 0 6 5"><path d="M.8 2.5l1.6 1.6L5.2.8" fill="none" stroke="#d2821c" stroke-width=".8"/></svg></div>
    <div class="faq-item" style="left:138px;top:95px"><h4>F.A.Q question number 3?</h4><p>Credibly evolve client-focused convergence rather than leveraged quality vectors. Authoritatively provide access to market-driven manufactured products with standardized.</p></div>
    <div class="faq-tick" style="left:307px;top:97px"><svg width="6" height="5" viewBox="0 0 6 5"><path d="M.8 2.5l1.6 1.6L5.2.8" fill="none" stroke="#d2821c" stroke-width=".8"/></svg></div>
    <div class="faq-item" style="left:324px;top:95px"><h4>F.A.Q question number 4?</h4><p>Laboriosam iusto quia nulla ad voluptatibus iste beatae voluptas corrupti facilis accusamus recusandae sequi debitis reprehenderit quibusdam. Facilis eligendi a.</p></div>
    <div class="to-top" style="left:579px;top:115px;background:#bdbdbd"><svg width="5" height="3" viewBox="0 0 5 3"><path d="M.5 2.5l2-2 2 2" fill="none" stroke="#fff" stroke-width=".7"/></svg></div>
  </section>

  <section class="band contact">
    <div class="photo" role="img" aria-label="Person doing a handstand on a riverside promenade near a bridge" style="left:320px;top:0;width:282px;height:185px;background:linear-gradient(90deg,rgba(228,232,236,0),rgba(205,190,170,.6) 40%,rgba(225,228,230,.4))"></div>
    <h3 style="left:84px">Subscribe to Newsletter</h3>
    <div class="field-label" style="top:55px">Your Name</div>
    <div class="field" style="top:67px"></div>
    <div class="field-label" style="top:94px">Your Email</div>
    <div class="field" style="top:105px"></div>
    <div class="outline-btn" style="top:131px">Subscribe</div>
    <div class="note">We Keep Your Information Secret</div>
    <h3 style="left:233px">Location:</h3>
    <div class="address">58 Harbour Row, Suite 12<br>Wellington 6011<br><br><b>Phone:</b> (04) 555 0192<br><b>Fax:</b> (04) 555 0193<br><b>Email:</b> hello@mistline.example</div>
    <div class="socials"><i></i><i style="background:#2aa3ef"></i><i></i><i></i></div>
  </section>

  <footer class="band footer">
    <p>Copyrights © 2019 All Rights Reserved by Mistline Co.</p>
    <p class="links">Terms of Use / Privacy Policy</p>
    <div class="to-top" style="left:579px;top:18px;background:#bdbdbd"><svg width="5" height="3" viewBox="0 0 5 3"><path d="M.5 2.5l2-2 2 2" fill="none" stroke="#fff" stroke-width=".7"/></svg></div>
  </footer>

</main>
</body>
</html>
```